Responsive WordPress website for medical therapy practice consulting business.

We need both design and website for responsive Wordpress website. The use of Tessaly theme is preferred when considering the design (not required).
Site must be designed for 1920px width and fully responsive.
See full scope of the project below.

DESIGN:
Design a full screen layout using images and parallax movement where appropriate.
Easy to use navigation for desktop and hamburger style navigation for mobile devices.
Create an original design for the home, sub-page template.
Create a responsive website using common desktop breakpoints 1920, 1366, 1280 1024 as well as mobile devices.
Color scheme should use soft or pastel color avoiding reds.
Design will take inspiration from logo design and color scheme.
Large “Hero slider” may be employed to striking visual interest.
The website will focus the content on the Homepage mission statement, What We Do and How to Reach Us, content.
Website Footer Information: Include content for Privacy Policy and Terms of Use, address and copyright information.

DEVELOPMENT NOTES:

WordPress content management platform will be used .

Responsive grid will be used to properly display website content on all devices including mobile, laptop and desktop at standard breakpoints.

Social Media links to LinkedIn and Twitter

Google Analytics and Search Console integration – allows tracking of visitors and in-depth search data, indexing and performance.

Yoast Basic SEO – basic setup and integration is included in the proposal. This includes creating SEO friendly page titles, search descriptions and best practices for heading and image tags.

508 & ADA compliance

PAGE LIST:
The following pages are a list of current websites pages. These are used as a guideline for developing the proposal and can be changed to reflect content:

NAVIGATION LINKS:

HOME

· Featuring the new logo, the home page will display Brenlow Care Advisor’s message, services, and contact information.
· The navigation will be prominent, intuitive and easy to use, allowing to find information quickly.
· Parallax scrolling will provide a cool modern visual effect without being overbearing.

====================================================

ABOUT US –

· History
· Bios
· Links

SERVICES

· Business Consultancy service

CONTACT US – This section will present ways for viewers to reach out either by phone, email.

· Google map of office locations.
· Business information
a. Locations
b. Address
c. Phone
d. Fax
e. Email

FOOTER LINKS – Additional information for legal or usage claims, company info and contact info.

· Copyright information
· Links to CONTACT
· Social Media
· Disclaimer
· Privacy policy
· Terms of use

```html
<!DOCTYPE html>
<html lang="en">
<head>
<meta charset="utf-8">
<title>Brenlow Care Advisors</title>
<link rel="stylesheet" href="https://fonts.googleapis.com/css2?family=Raleway:wght@500;600;700;800&family=Open+Sans:ital,wght@0,400;0,600;0,700;1,400&family=Montserrat:wght@500;600;700&display=swap">
<style>
:root{
  --blue:#5f86c4;
  --blue-band:#6a8bc3;
  --blue-deep:#3f6db3;
  --ink:#505050;
  --text:#6b6b6b;
  --pale:#eef1fb;
  --white:#ffffff;
  --ring:#cfcfcf;
  --map-land:#f3e4e4;
  --map-sea:#9cc4ef;
}
*{box-sizing:border-box;margin:0;padding:0}
html,body{width:1200px;height:3077px;overflow:hidden}
body{font-family:"Open Sans",Arial,sans-serif;color:var(--text);background:var(--white);position:relative}
.site-header{height:90px;display:flex;align-items:center;justify-content:space-between;padding:0 122px 0 125px;background:var(--white);box-shadow:0 1px 4px rgba(0,0,0,.06);position:relative;z-index:2}
.brand{display:flex;align-items:center;gap:12px;font-family:"Raleway",sans-serif;font-weight:700;font-size:24px;color:var(--blue-deep)}
.brand-mark{width:34px;height:34px;border:2px solid var(--blue-deep)}
.main-nav{display:flex;align-items:center;gap:32px;font-family:"Montserrat",sans-serif;font-weight:600;font-size:12.5px;color:#222}
.main-nav .is-active{color:var(--blue)}
.hero{height:581px;position:relative;text-align:center;color:var(--white);overflow:hidden}
.hero-photo{position:absolute;inset:0;background:linear-gradient(100deg,#6f7d95 0%,#b9b7b4 28%,#e2ddd6 52%,#d6cfc5 72%,#a89f95 100%)}
.hero-photo::after{content:"";position:absolute;inset:0;background:rgba(40,45,60,.25)}
.hero-content{position:relative;padding-top:160px}
.hero-title{font-family:"Raleway",sans-serif;font-weight:700;font-size:54px;letter-spacing:.5px;line-height:1.2}
.hero-sub{font-size:22px;margin-top:12px}
.btn-outline{display:inline-block;border:2px solid currentColor;border-radius:24px;font-family:"Montserrat",sans-serif;font-weight:700;font-size:12px;letter-spacing:.5px;text-transform:uppercase}
.hero .btn-outline{margin-top:30px;padding:13px 34px;color:var(--white)}
.slider-dots{position:absolute;left:0;right:0;top:520px;display:flex;justify-content:center;gap:5px}
.slider-dots span{width:10px;height:10px;border-radius:50%;border:2px solid var(--white)}
.slider-dots span:first-child{background:var(--white)}
.mission{height:238px;background:var(--blue-band);color:var(--white);text-align:center;padding-top:46px}
.section-title{font-family:"Raleway",sans-serif;font-weight:700;font-size:38px;color:var(--ink);line-height:1.2}
.mission .section-title{color:var(--white)}
.mission p{width:680px;margin:16px auto 0;font-size:12px;line-height:22px}
.about{height:587px;text-align:center;padding-top:82px}
.about-intro{width:720px;margin:22px auto 0;font-size:12px;line-height:27px}
.pillars{display:flex;justify-content:center;margin-top:40px}
.pillar{width:332px}
.pillar-icon{width:104px;height:104px;border:2px solid var(--ring);border-radius:50%;margin:0 auto;display:flex;align-items:center;justify-content:center}
.pillar h3{font-family:"Raleway",sans-serif;font-weight:600;font-size:20px;color:var(--ink);margin-top:24px}
.pillar p{width:290px;margin:12px auto 0;font-size:12px;line-height:21px}
.read-link{display:inline-block;margin-top:16px;font-family:"Montserrat",sans-serif;font-weight:700;font-size:12px;color:var(--blue)}
.services{height:505px;background:var(--pale);display:flex;justify-content:space-between;padding:84px 126px 0 124px}
.services-copy{width:440px}
.services-copy .section-title{text-align:left}
.services-copy .services-sub{font-family:"Raleway",sans-serif;font-weight:600;font-size:28px;line-height:1.2;color:var(--blue);margin-top:12px}
.services-copy .services-body{font-size:12.5px;line-height:23.5px;margin-top:30px}
.services .btn-outline{margin-top:32px;padding:12px 26px;color:var(--blue);background:var(--white)}
.video-frame{width:454px;height:323px;margin-top:3px;border:5px solid var(--white);box-shadow:0 1px 6px rgba(0,0,0,.12);position:relative;background:linear-gradient(135deg,#5e6670 0%,#c9ced6 40%,#eef0f3 70%,#9aa3ad 100%)}
.play{position:absolute;left:50%;top:50%;width:58px;height:58px;margin:-29px 0 0 -29px;border-radius:50%;background:rgba(30,30,30,.8);display:flex;align-items:center;justify-content:center}
.reach{height:711px;position:relative;text-align:center;padding-top:92px}
.map{position:absolute;left:0;right:0;top:296px;height:415px;background:linear-gradient(100deg,var(--map-sea) 0%,var(--map-land) 10%,var(--map-land) 62%,var(--map-sea) 70%,#b8d6f5 100%)}
.contact-card{position:absolute;left:124px;top:206px;width:950px;height:124px;background:var(--white);box-shadow:0 2px 8px rgba(0,0,0,.18);display:flex;align-items:center;padding:0 28px;z-index:1;text-align:left}
.contact-item{display:flex;align-items:center;gap:22px;font-size:12px;line-height:20px;color:var(--text)}
.contact-item:nth-child(1){width:240px}
.contact-item:nth-child(2){width:228px}
.contact-item:nth-child(3){width:175px}
.contact-icon{width:46px;height:46px;border:2px solid #d4d4d4;border-radius:50%;display:flex;align-items:center;justify-content:center;flex:none}
.site-footer{text-align:center;padding-top:93px}
.btn-solid{display:inline-block;background:var(--blue);color:var(--white);border-radius:24px;padding:15px 28px;font-family:"Montserrat",sans-serif;font-weight:700;font-size:12.5px;letter-spacing:.5px}
.copyright{font-size:13px;margin-top:26px;color:var(--text)}
.social{display:flex;justify-content:center;gap:10px;margin-top:22px}
.social a{width:34px;height:34px;border:2px solid var(--ring);border-radius:50%;display:flex;align-items:center;justify-content:center}
.social a span{width:8px;height:8px;border-radius:50%;background:var(--blue)}
.disclaimer{width:620px;margin:22px auto 0;font-size:9.5px;line-height:19px;color:var(--text)}
.disclaimer em{font-weight:600}
</style>
</head>
<body>
<header class="site-header">
  <div class="brand"><span class="brand-mark"></span>Brenlow Care Advisors</div>
  <nav class="main-nav">
    <span class="is-active">HOME</span><span>ABOUT US</span><span>SERVICES</span><span>CONTACT US</span>
    <svg width="14" height="14" viewBox="0 0 14 14"><circle cx="5.5" cy="5.5" r="4" fill="none" stroke="#222" stroke-width="2"/><line x1="8.5" y1="8.5" x2="12.5" y2="12.5" stroke="#222" stroke-width="2.2"/></svg>
  </nav>
</header>

<section class="hero">
  <div class="hero-photo" role="img" aria-label="Photo of a hand writing notes on a clipboard during a therapy session"></div>
  <div class="hero-content">
    <h1 class="hero-title">BRENLOW CARE ADVISOR</h1>
    <p class="hero-sub">At vero eos et accusamus et iusto odio dignissimos duotas ass</p>
    <span class="btn-outline">Get more info</span>
  </div>
  <div class="slider-dots"><span></span><span></span><span></span><span></span></div>
</section>

<section class="mission">
  <h2 class="section-title">MISSION STATEMENT</h2>
  <p>Nam libero tempore, cum soluta nobis est eligendi optio cumque nihil impedit quo minus id quod maxime placeat facere possimus, omnis voluptas assumenda est, omnis dolor repellendus. Temporibus autem quibusdam et aut officiis debitis aut rerum necessitatibus saepe eveniet ut et voluptates repudiandae sint et molestiae ut</p>
</section>

<section class="about">
  <h2 class="section-title">ABOUT BCA</h2>
  <p class="about-intro">Nam libero tempore, cum soluta nobis est eligendi optio cumque nihil impedit quo minus id quod maxime placeat facere possimus, omnis voluptas assumenda esom nis dolor repellen dus mporibus autdi tempora inciduem quibusdam et aut of</p>
  <div class="pillars">
    <div class="pillar">
      <div class="pillar-icon"><svg width="48" height="48" viewBox="0 0 48 48"><circle cx="24" cy="24" r="23" fill="var(--blue)"/><circle cx="24" cy="13" r="3.5" fill="#fff"/><rect x="20" y="20" width="8" height="17" rx="1" fill="#fff"/><rect x="17" y="35" width="14" height="3" fill="#fff"/></svg></div>
      <h3>History</h3>
      <p>Sed ut perspiciatis unde omnis iste natsit volupta tem accusantium dolorem ipsam voluptatem quia volu ptas sit aspernatur aut odit auted quia</p>
      <span class="read-link">READ MORE</span>
    </div>
    <div class="pillar">
      <div class="pillar-icon"><svg width="52" height="44" viewBox="0 0 52 44"><g fill="var(--blue)"><circle cx="26" cy="9" r="7"/><circle cx="12" cy="14" r="5.5"/><circle cx="40" cy="14" r="5.5"/><path d="M15 40c0-10 5-16 11-16s11 6 11 16z"/><path d="M2 38c0-8 4-13 10-13 3 0 5 1 6 3-3 3-4 6-4 10z"/><path d="M50 38c0-8-4-13-10-13-3 0-5 1-6 3 3 3 4 6 4 10z"/></g></svg></div>
      <h3>Bios</h3>
      <p>Sed ut perspiciatis unde omnis iste natsit volupta tem accusantium dolorem ipsam voluptatem quia volu ptas sit aspernatur aut odit auted quia</p>
      <span class="read-link">READ MORE</span>
    </div>
    <div class="pillar">
      <div class="pillar-icon"><svg width="50" height="30" viewBox="0 0 50 30"><path d="M2 15C10 4 18 1 25 1s15 3 23 14C40 26 32 29 25 29S10 26 2 15z" fill="none" stroke="var(--blue)" stroke-width="3"/><circle cx="25" cy="15" r="8" fill="var(--blue)"/><circle cx="22" cy="12" r="2.5" fill="#fff"/></svg></div>
      <h3>Vision</h3>
      <p>Sed ut perspiciatis unde omnis iste natsit volupta tem accusantium dolorem ipsam voluptatem quia volu ptas sit aspernatur aut odit auted quia</p>
      <span class="read-link">READ MORE</span>
    </div>
  </div>
</section>

<section class="services">
  <div class="services-copy">
    <h2 class="section-title">SERVICES</h2>
    <p class="services-sub">Business Consultancy service</p>
    <p class="services-body">Nam libero tempore, cum soluta nobis est eligendi optio cumque nihil impedit quo minus id quod maxime placeat facere possimus, omnis voluptas assumenda esom nis dolor repellen dus. Temporibus autem quibusdam et aut officiis debitis aut rer um necessitatibus saepe eve niet ut et voluptates repudiandae sint et molesbanon recusandae. Itaque earum rerum hic tenetur a sapiente delectus, ut aut reiciendis voluptatibus maiores alias consequatur aup.</p>
    <span class="btn-outline">Read more</span>
  </div>
  <div class="video-frame" role="img" aria-label="Video still of a medical team meeting around a table">
    <div class="play"><svg width="20" height="22" viewBox="0 0 20 22"><path d="M3 1l16 10L3 21z" fill="#fff"/></svg></div>
  </div>
</section>

<section class="reach">
  <h2 class="section-title">HOW TO REACH US</h2>
  <div class="contact-card">
    <div class="contact-item">
      <span class="contact-icon"><svg width="16" height="20" viewBox="0 0 16 20"><path d="M8 1a7 7 0 0 1 7 7c0 5-7 11-7 11S1 13 1 8a7 7 0 0 1 7-7z" fill="var(--blue)"/><circle cx="8" cy="8" r="2.6" fill="#fff"/></svg></span>
      <span>48 Larkfield Road<br>Ashcombe NSW 2790</span>
    </div>
    <div class="contact-item">
      <span class="contact-icon"><svg width="18" height="18" viewBox="0 0 18 18"><path d="M4 1l3 4-2 2c1 3 3 5 6 6l2-2 4 3-2 3C8 17 1 10 1 3z" fill="var(--blue)"/></svg></span>
      <span>1 800 555 0142</span>
    </div>
    <div class="contact-item">
      <span class="contact-icon"><svg width="18" height="18" viewBox="0 0 18 18"><rect x="4" y="1" width="10" height="5" fill="var(--blue)"/><rect x="1" y="6" width="16" height="11" rx="1" fill="var(--blue)"/><rect x="5" y="10" width="8" height="5" fill="#fff"/></svg></span>
      <span>1 800 555 0199</span>
    </div>
    <div class="contact-item">
      <span class="contact-icon"><svg width="20" height="16" viewBox="0 0 20 16"><rect x="1" y="1" width="18" height="14" rx="1.5" fill="var(--blue)"/><path d="M1.5 2l8.5 7 8.5-7" fill="none" stroke="#fff" stroke-width="1.6"/></svg></span>
      <span>info@brenlowcareadvisors.com</span>
    </div>
  </div>
  <div class="map" role="img" aria-label="Map of office locations across the region"></div>
</section>

<footer class="site-footer">
  <span class="btn-solid">CONTACT US</span>
  <p class="copyright">Brenlow Care Advisors © 2019 All rights reserved. Privacy policy &nbsp;|&nbsp; Terms of use</p>
  <div class="social">
    <a aria-label="Social profile"><span></span></a>
    <a aria-label="Professional network profile"><span></span></a>
  </div>
  <p class="disclaimer"><em>Disclaimer:</em> Nemo enim ipsam voluptatem quia voluptas sit aspernatur aut odit aut fugit, sed quia consequuntur magni dolores eos quals one voluptatem sequi nesciunt. Neque porro quisquam est, qui dolorem ipsum quia dolor sit amet, consectetur, adipisci velit, sed quia non numquam eius modi tempora incidunt ut labore et dolore magnam aliquam quaerat voluptatem.</p>
</footer>
</body>
</html>
```